Valmuna - Plant extraction for human use

Valmuna is a plant extraction based on long pepper containing a high concentration of piperlongumine. Piperlongumine has mainly anti-cancer properties, shown in many animal studies (200). It has as well shown to inhibit dementia and bone inflammation (in animal studies). We are the first to offer this extract for the European market. Because the product will be sold under a ‘plant extraction’ legislation, we cannot make any claims about the medical properties of the extract. I need a design for the packaging (blister pack) in a category for life enhancing medicine with no connotation of cancer for the European market in a first phase. We target people from 35-75 years old. For the younger group of people, we would propose (without saying) to use our product for chemoprevention against cancer. For those patients which have been diagnosed with cancer, we would propose to use it in conjunction with chemo-radio or immunotherapy (without saying).
Target Market(s)
Europe
Look and feel

```html
<!DOCTYPE html>
<html lang="en">
<head>
<meta charset="utf-8">
<title>Valmuna – Packaging Front</title>
<link rel="stylesheet" href="https://fonts.googleapis.com/css2?family=Dosis:wght@700&family=Montserrat:wght@300;400&display=swap">
<style>
  :root {
    --bg: #ffffff;
    --silver-light: #f1f1f2;
    --silver-mid: #dcdcde;
    --silver-dark: #c9c9cc;
    --brand-blue: #2f9fd8;
    --accent-green: #8ab92d;
    --white: #ffffff;
    --ribbon-orange: #f0961e;
    --ribbon-blue: #1f5fae;
    --ribbon-teal: #3fb3c4;
    --ribbon-magenta: #c8287e;
    --ribbon-purple: #5a2a8c;
  }
  html, body {
    margin: 0;
    padding: 0;
    width: 1200px;
    height: 945px;
    overflow: hidden;
    background: var(--bg);
  }
  .canvas {
    position: relative;
    width: 1200px;
    height: 945px;
  }
  .pack-front {
    position: absolute;
    left: 100px;
    top: 150px;
    width: 1000px;
    height: 660px;
    overflow: hidden;
    background: linear-gradient(135deg, var(--silver-light) 0%, var(--silver-mid) 55%, var(--silver-dark) 100%);
  }
  .ribbon-art {
    position: absolute;
    left: -40px;
    top: 84px;
    width: 660px;
    height: 500px;
    border-radius: 48% 52% 40% 60% / 55% 45% 55% 45%;
    background:
      radial-gradient(ellipse at 70% 85%, rgba(200,40,126,0.55) 0%, rgba(200,40,126,0) 45%),
      radial-gradient(ellipse at 45% 20%, rgba(31,95,174,0.55) 0%, rgba(31,95,174,0) 45%),
      radial-gradient(ellipse at 10% 70%, rgba(90,42,140,0.5) 0%, rgba(90,42,140,0) 40%),
      radial-gradient(ellipse at 40% 60%, rgba(240,150,30,0.6) 0%, rgba(63,179,196,0.25) 45%, rgba(240,150,30,0) 70%);
    opacity: 0.85;
  }
  .tagline {
    position: absolute;
    right: 200px;
    top: 205px;
    margin: 0;
    font-family: "Montserrat", sans-serif;
    font-weight: 400;
    font-size: 21px;
    line-height: 40px;
    color: var(--brand-blue);
    text-align: right;
    letter-spacing: 0.2px;
  }
  .product-name {
    position: absolute;
    right: 200px;
    top: 300px;
    margin: 0;
    font-family: "Dosis", sans-serif;
    font-weight: 700;
    font-size: 180px;
    line-height: 180px;
    color: var(--brand-blue);
    letter-spacing: 1px;
  }
  .category-band {
    position: absolute;
    left: 406px;
    top: 494px;
    width: 394px;
    height: 54px;
    background: var(--accent-green);
    display: flex;
    align-items: center;
    justify-content: center;
    font-family: "Montserrat", sans-serif;
    font-weight: 300;
    font-size: 27px;
    color: var(--white);
    letter-spacing: 0.5px;
    white-space: nowrap;
  }
</style>
</head>
<body>
  <main class="canvas">
    <section class="pack-front">
      <div class="ribbon-art" role="img" aria-label="Flowing multicoloured ribbon loop in orange, blue, teal, magenta and purple"></div>
      <p class="tagline">Plant extraction based on long pepper containing<br>a high concentration of piperlongumine.</p>
      <h1 class="product-name">Valmuna</h1>
      <div class="category-band">LIFE ENHANCING MEDICINE</div>
    </section>
  </main>
</body>
</html>
```